Glass window Vinyl

We are in need of window vinyls for the building shown in the photos. The current vinyls will come down, and we will install the new signage created by this process. We need to advertise:

"Harwell's Landing Pop Up Market"

Then, below that, it should say for rental inquiries call : 555.613.0872 with our logo which is attached along with our colors and brand guidelines. You may add more color to the Harwells landing pop up market signage if appropriate. It should be large enough to be easily read from the road by those passing by.

```html
<!DOCTYPE html>
<html lang="en">
<head>
<meta charset="utf-8">
<title>Harwell's Landing Pop Up Market – Window Vinyl</title>
<link rel="stylesheet" href="https://fonts.googleapis.com/css2?family=Anton&display=swap">
<style>
  :root {
    --navy: #2a2a75;
    --red: #df3147;
    --charcoal: #2f3233;
    --white: #ffffff;
    --ink: #123f47;
  }
  * { margin: 0; padding: 0; box-sizing: border-box; }
  html, body { width: 1108px; height: 1200px; overflow: hidden; background: var(--white); }
  .vinyl { position: relative; width: 1108px; height: 1200px; font-family: "Anton", "Arial Narrow", sans-serif; }

  .header-band {
    position: absolute; left: 0; top: 0; width: 1108px; height: 337px;
    background: var(--navy);
  }
  .market-name { position: absolute; left: 0; top: 0; width: 1108px; height: 337px; }
  .market-name text { font-family: "Anton", "Arial Narrow", sans-serif; text-anchor: middle; }
  .market-name .place { fill: var(--red); font-size: 118px; }
  .market-name .event { fill: var(--white); font-size: 118px; }

  .window-band {
    position: absolute; left: 0; top: 337px; width: 1108px; height: 490px;
    background: var(--charcoal);
  }

  .inquiry-bar {
    position: absolute; left: 55px; top: 827px; width: 997px; height: 122px;
    background: var(--red);
  }
  .inquiry-bar svg { width: 100%; height: 100%; }
  .inquiry-bar text { fill: var(--white); font-family: "Anton", "Arial Narrow", sans-serif; font-size: 66px; text-anchor: middle; }

  .company-name {
    position: absolute; left: 55px; top: 1020px; width: 400px;
    color: var(--ink); text-align: center; line-height: 1;
    display: flex; flex-direction: column; align-items: center; gap: 8px;
  }
  .company-name .mark { width: 26px; height: 26px; background: var(--ink); }
  .company-name .primary { font-size: 38px; letter-spacing: 6px; }
  .company-name .secondary { font-size: 16px; letter-spacing: 8px; }

  .phone-icon { position: absolute; left: 491px; top: 1015px; width: 79px; height: 79px; }
  .phone-number { position: absolute; left: 592px; top: 1005px; width: 462px; height: 100px; }
  .phone-number text { fill: var(--navy); font-family: "Anton", "Arial Narrow", sans-serif; font-size: 96px; }
</style>
</head>
<body>
<main class="vinyl">
  <section class="header-band">
    <svg class="market-name" viewBox="0 0 1108 337" aria-label="Harwell's Landing Pop Up Market">
      <text class="place" x="554" y="157" textLength="908" lengthAdjust="spacingAndGlyphs">HARWELL'S LANDING</text>
      <text class="event" x="554" y="281" textLength="704" lengthAdjust="spacingAndGlyphs">POP UP MARKET</text>
    </svg>
  </section>

  <section class="window-band"></section>

  <section class="inquiry-bar">
    <svg viewBox="0 0 997 122">
      <text x="498" y="87" textLength="757" lengthAdjust="spacingAndGlyphs">FOR RENTAL INQUIRIES CALL:</text>
    </svg>
  </section>

  <div class="company-name">
    <span class="mark"></span>
    <span class="primary">BRAMBLE ROW</span>
    <span class="secondary">PROPERTIES</span>
  </div>

  <svg class="phone-icon" viewBox="0 0 80 80" aria-hidden="true">
    <circle cx="40" cy="40" r="40" fill="var(--navy)"/>
    <path d="M27 18c3 0 7 8 7 10s-4 4-4 6c0 4 10 14 14 14 2 0 4-4 6-4s10 4 10 7c0 4-5 9-10 9-14 0-33-19-33-33 0-5 5-9 10-9z" fill="var(--white)"/>
    <path d="M46 22a14 14 0 0 1 12 12M46 14a22 22 0 0 1 20 20" fill="none" stroke="var(--white)" stroke-width="4" stroke-linecap="round"/>
  </svg>

  <svg class="phone-number" viewBox="0 0 462 100">
    <text x="0" y="92" textLength="460" lengthAdjust="spacingAndGlyphs">555.613.0872</text>
  </svg>
</main>
</body>
</html>
```